Online Marketing Agency Website

We are an online marketing agency that specializes in search marketing (SEM) for businesses of all sizes. Our core services include local search marketing, seo, paid search, paid social, graphic design, video production/editing and website design. We have an existing website that we launched a number of years ago but it's very outdated and we're currently too busy to design a new version.

Target Market(s)

Any business that needs online marketing services with an emphasis on search marketing.

Industry/Entity Type

Ad Agency

Number of Pages Required

4 page

Font styles to use
Sans Serif

Requirements
Must have
• Home page, interior page, blog page, contact us page.
Look and feel should be modern and clean and easy to navigate.
Sections for call outs for specific services: Business Marketing Strategy, Content Creation and Marketing, Graphic & Publication Design, Pay Per Click (PPC) Management, Search Engine Optimization, Social Media Management, Video Production & Editing, Website Hosting & Management, Website Design & Development
Use color from logo that was uploaded.

```html
<!DOCTYPE html>
<html lang="en">
<head>
<meta charset="utf-8">
<title>Liftpoint Media – About</title>
<link rel="stylesheet" href="https://fonts.googleapis.com/css2?family=Montserrat:wght@400;500;600;700&family=Rajdhani:wght@700&display=swap">
<style>
:root{
  --accent:#f2654a;
  --accent-strong:#ef4f2c;
  --ink:#222222;
  --text:#333333;
  --muted:#6a6a6a;
  --blush:#fbe4e0;
  --line:#f0d8d2;
  --paper:#ffffff;
}
*{box-sizing:border-box;margin:0;padding:0}
html,body{width:1200px;height:2184px;overflow:hidden;background:var(--paper)}
body{font-family:'Montserrat',sans-serif;color:var(--text)}
.page{position:relative;width:1200px;height:2184px;overflow:hidden;background:var(--paper)}
.backdrop{position:absolute;left:0;top:0;width:1200px;height:2184px}

/* header */
.site-header{position:absolute;left:0;top:0;width:1200px;height:139px;background:var(--paper);box-shadow:0 2px 8px rgba(0,0,0,.06);z-index:3}
.nav{position:absolute;top:90px;display:flex;gap:22px;font-size:14px;font-weight:500;color:var(--ink)}
.nav a{color:inherit;text-decoration:none}
.nav .active{color:var(--accent-strong);font-weight:600}
.nav-left{left:264px}
.nav-right{left:735px}
.brand{position:absolute;left:467px;width:240px;text-align:center;color:var(--ink);white-space:nowrap}
.brand-mark{display:block;width:30px;height:30px;border-radius:50%;background:var(--accent-strong);margin:0 auto 30px}
.brand-name{font-size:18px;font-weight:700;letter-spacing:.3px;line-height:20px}
.brand-tag{font-size:11.5px;font-weight:500;line-height:14px}

/* hero */
.hero{position:absolute;left:0;top:139px;width:1200px;height:128px;background:linear-gradient(90deg,#fdeeeb,#fbdcd5 45%,#f8d6cf 60%,#fce8e4)}
.hero-title{position:absolute;left:0;top:185px;width:1200px;text-align:center;font-size:22px;font-weight:700;color:var(--ink);z-index:2}

/* intro */
.intro-visual{position:absolute;left:180px;top:315px;width:328px;height:336px;border-radius:14px;background:linear-gradient(160deg,#c9d6e2 0%,#eef1f4 45%,#f3c3b8 75%,#d84b33 100%)}
.intro-heading{position:absolute;left:545px;top:322px;font-size:21px;font-weight:700;line-height:26px;color:var(--ink)}
.intro-copy{position:absolute;left:547px;top:395px;width:470px;font-size:12px;line-height:18.8px;color:var(--text)}

.section-title{position:absolute;left:0;width:1200px;text-align:center;font-weight:700;color:var(--ink)}
.who-copy{position:absolute;left:210px;width:780px;text-align:center;font-size:13.6px;line-height:16.3px;color:var(--text)}

/* writers */
.carousel-arrow{position:absolute;top:1107px;width:14px;height:22px}
.writer{position:absolute;top:1020px;width:203px;text-align:center}
.writer-photo{width:203px;height:195px}
.writer-bar{height:3px;background:var(--accent);margin-top:5px}
.writer-name{font-size:14.5px;font-weight:600;color:var(--ink);margin-top:17px}
.writer-bio{font-size:10.2px;line-height:13px;color:var(--muted);margin:7px auto 0;width:150px}
.btn-more{display:inline-block;margin-top:13px;width:82px;height:27px;line-height:25px;border-radius:14px;border:1.5px solid var(--accent);font-size:10px;color:var(--text)}
.btn-more.filled{background:var(--accent);color:#fff}

/* cta */
.cta{position:absolute;left:0;top:1417px;width:1200px;height:280px;background:linear-gradient(100deg,#fbe8e4,#f8ddd6 50%,#f6d2c9)}
.cta-title{position:absolute;left:0;top:1494px;width:1200px;text-align:center;font-size:26.5px;font-weight:700;color:#111;letter-spacing:.3px}
.cta-sub{position:absolute;left:0;top:1527px;width:1200px;text-align:center;font-size:16px;color:var(--text)}
.field{position:absolute;top:1569px;height:46px;background:#fff;border-radius:23px;border:1px solid var(--line);display:flex;align-items:center;padding-left:24px;font-size:13.5px;color:#555}
.field svg{position:absolute;right:18px;top:14px}
.submit{position:absolute;left:794px;top:1570px;width:149px;height:45px;border-radius:23px;background:var(--accent);color:#fff;font-family:'Rajdhani',sans-serif;font-weight:700;font-size:17px;letter-spacing:.5px;text-align:center;line-height:45px}

/* footer */
.contact-item{position:absolute;top:1970px}
.contact-label{font-size:13px;font-weight:600;color:var(--ink)}
.contact-value{font-size:12px;line-height:14.5px;color:var(--text);margin-top:13px}
.contact-icon{position:absolute;top:1970px}
.copyright{position:absolute;left:0;top:2098px;width:1200px;text-align:center;font-size:13px;color:var(--accent)}
</style>
</head>
<body>
<div class="page">

  <svg class="backdrop" viewBox="0 0 1200 2184" aria-hidden="true">
    <defs>
      <linearGradient id="curveShade" x1="0" y1="0" x2="1" y2="0">
        <stop offset="0" stop-color="#eeeeee"/>
        <stop offset="1" stop-color="#ffffff"/>
      </linearGradient>
      <linearGradient id="curveShadeR" x1="1" y1="0" x2="0" y2="0">
        <stop offset="0" stop-color="#e9e9e9"/>
        <stop offset="1" stop-color="#ffffff"/>
      </linearGradient>
    </defs>
    <path d="M1200 325 C1110 330 1030 345 1060 410 L1200 625 Z" fill="url(#curveShadeR)" opacity=".9"/>
    <path d="M0 690 L80 790 C110 830 90 870 40 880 L0 885 Z" fill="url(#curveShade)"/>
    <path d="M0 815 L48 875 C70 905 55 935 20 940 L0 942 Z" fill="var(--accent)"/>
    <path d="M0 1825 L170 1780 C220 1765 225 1720 190 1697 L0 1697 Z" fill="#ffffff" stroke="#f2ecec" stroke-width="1"/>
    <path d="M1200 1885 C1090 1900 1010 1935 1070 2010 L1200 2140 Z" fill="url(#curveShadeR)" opacity=".9"/>
  </svg>

  <header class="site-header">
    <nav class="nav nav-left"><a href="#">Home</a><a href="#">Services</a><a href="#" class="active">About</a></nav>
    <div class="brand" style="top:22px">
      <span class="brand-mark"></span>
      <div class="brand-name">LIFTPOINT MEDIA</div>
      <div class="brand-tag">Search Marketing. Simplified</div>
    </div>
    <nav class="nav nav-right"><a href="#">Testimonials</a><a href="#">Blog</a><a href="#">Contact</a></nav>
  </header>

  <div class="hero" role="img" aria-label="Soft illustration of a smiling team of three people and a mail icon"></div>
  <h1 class="hero-title">About us</h1>

  <div class="intro-visual" role="img" aria-label="Rocket launching upward from a rising red growth line in front of office buildings"></div>
  <h2 class="intro-heading">Liftpoint Media<br>online marketing services</h2>
  <p class="intro-copy">Sed ut perspiciatis unde omnis iste natus error sit voluptatem accusantium doloremque laudantium, totam rem aperiam, eaque ipsa quae ab illo inventore veritatis et quasi architecto beatae vitae dicta sunt explicabo. Nemo enim ipsam voluptatem quia voluptas sit aspernatur aut odit aut fugit, sed quia consequuntur magni dolores eos qui ratione voluptatem sequi nesciunt. Neque porro quisquam est, qui dolorem ipsum quia dolor sit amet, consectetur, adipisci velit, sed quia non numquam eius modi tempora incidunt ut labore et dolore magnam aliquam quaerat voluptatem. Ut enim ad minima veniam, quis nostrum exercitationem ullam corporis suscipit laboriosam, nisi ut aliquid ex ea commodi consequatur Quis autem vel eum iure reprehenderit qui in ea voluptate velit esse quam nihil molestiae consequatur, vel illum qui dolorem eum fugiat quo voluptas nulla pariatur quasi architecto beatae vitae dicta sunt explicabo.</p>

  <h2 class="section-title" style="top:707px;font-size:21px">Who We Are</h2>
  <p class="who-copy" style="top:764px">vero eos et accusamus et iusto odio dignissimos ducimus qui blanditiis praesentium voluptatum deleniti atque corrupti quos dolores et quas molestias excepturi sint occaecati cupiditate non provident, similique sunt in culpa qui officia deserunt mollitia animi, id est laborum et dolorum fuga. Et harum quidem rerum facilis est et expedita distinctio.</p>
  <p class="who-copy" style="top:845px">Nam libero tempore, cum soluta nobis est eligendi optio cumque nihil impedit quo minus id quod maxime placeat facere possimus, omnis voluptas assumenda est, omnis dolor repellendus. Temporibus autem quibus-dam et aut officiis debitis aut rerum necessitatibus saepe eveniet ut et voluptates repudiandae</p>

  <h2 class="section-title" style="top:960px;font-size:23px">Meet a Few of Our Writers</h2>

  <svg class="carousel-arrow" style="left:136px" viewBox="0 0 14 22" aria-hidden="true"><path d="M11 2 L3 11 L11 20" fill="none" stroke="#555" stroke-width="1.8"/></svg>
  <svg class="carousel-arrow" style="left:1043px" viewBox="0 0 14 22" aria-hidden="true"><path d="M3 2 L11 11 L3 20" fill="none" stroke="var(--accent)" stroke-width="1.8"/></svg>

  <article class="writer" style="left:182px">
    <div class="writer-photo" role="img" aria-label="Portrait photo of writer Marcus Hale" style="background:linear-gradient(180deg,#d9d9d9,#b9b3ae)"></div>
    <div class="writer-bar"></div>
    <div class="writer-name">Marcus Hale</div>
    <p class="writer-bio">Marcus is a<br>CPA and specializes in<br>small business</p>
    <span class="btn-more filled">Read More</span>
  </article>
  <article class="writer" style="left:393px">
    <div class="writer-photo" role="img" aria-label="Portrait photo of writer Nina Castell" style="background:linear-gradient(180deg,#a7aaa4,#6b5a4c 60%,#1f1f22)"></div>
    <div class="writer-bar"></div>
    <div class="writer-name">Nina Castell</div>
    <p class="writer-bio">Nina Castell specializes<br>in the full cycle of Human<br>Resource topics from</p>
    <span class="btn-more">Read More</span>
  </article>
  <article class="writer" style="left:604px">
    <div class="writer-photo" role="img" aria-label="Portrait photo of writer Owen Brandt" style="background:linear-gradient(180deg,#bfb2a2,#d8c7b5 55%,#e6e9ef)"></div>
    <div class="writer-bar"></div>
    <div class="writer-name">Owen Brandt</div>
    <p class="writer-bio">Owen Brandt's<br>professional background is<br>deeply rooted in financial</p>
    <span class="btn-more">Read More</span>
  </article>
  <article class="writer" style="left:814px">
    <div class="writer-photo" role="img" aria-label="Portrait photo of writer Peter Lindqvist" style="background:linear-gradient(180deg,#b9c1c6,#a08c7e 55%,#8fa6bf)"></div>
    <div class="writer-bar"></div>
    <div class="writer-name">Peter Lindqvist</div>
    <p class="writer-bio">Peter Lindqvist is a staff<br>writer at Growth Ledger<br>and editor of the</p>
    <span class="btn-more">Read More</span>
  </article>

  <section class="cta" role="img" aria-label="Faded photo of hands working on a laptop"></section>
  <h2 class="cta-title">GET FREE WEBSITE SEO SCORE ONLINE</h2>
  <p class="cta-sub">Enter your email to get the same cheatsheet for SEO.</p>
  <div class="field" style="left:255px;width:272px">Enter your website URL
    <svg width="18" height="18" viewBox="0 0 18 18" aria-hidden="true"><g fill="none" stroke="#777" stroke-width="1"><circle cx="9" cy="9" r="8"/><ellipse cx="9" cy="9" rx="3.5" ry="8"/><path d="M1 9h16M2.5 5h13M2.5 13h13"/></g></svg>
  </div>
  <div class="field" style="left:521px;width:280px">Enter your Email
    <svg width="20" height="16" viewBox="0 0 20 16" aria-hidden="true"><g fill="none" stroke="#666" stroke-width="1.2"><rect x="1" y="1" width="18" height="13"/><path d="M1 1l9 7 9-7M1 14l6-6M19 14l-6-6"/></g></svg>
  </div>
  <div class="submit">SUBMIT NOW</div>

  <div class="brand" style="top:1770px">
    <span class="brand-mark"></span>
    <div class="brand-name">LIFTPOINT MEDIA</div>
    <div class="brand-tag">Search Marketing. Simplified</div>
  </div>

  <svg class="contact-icon" style="left:265px" width="24" height="32" viewBox="0 0 24 32" aria-hidden="true"><path d="M12 1C6 1 1.5 5.5 1.5 11.5 1.5 19 12 31 12 31s10.5-12 10.5-19.5C22.5 5.5 18 1 12 1z" fill="var(--accent)"/><circle cx="12" cy="11.5" r="4" fill="#fff"/></svg>
  <div class="contact-item" style="left:310px">
    <div class="contact-label">Address Information</div>
    <div class="contact-value">58 Orchard Lane, Riverton,<br>NY 10872</div>
  </div>

  <svg class="contact-icon" style="left:554px;top:1974px" width="32" height="26" viewBox="0 0 32 26" aria-hidden="true"><g fill="none" stroke="var(--accent)" stroke-width="1.8"><rect x="1" y="1" width="26" height="19"/><path d="M1 1l13 10 13-10M1 20l9-8"/></g><circle cx="26" cy="19" r="5" fill="var(--accent)"/></svg>
  <div class="contact-item" style="left:604px">
    <div class="contact-label">Email Address</div>
    <div class="contact-value">hello@liftpointmedia.com</div>
  </div>

  <svg class="contact-icon" style="left:793px" width="28" height="28" viewBox="0 0 28 28" aria-hidden="true"><path d="M6 2l5 6-3 3c1.5 3.5 4.5 6.5 8 8l3-3 6 5-3 4C13 24 4 15 2 5z" fill="var(--accent)"/><path d="M17 2v8M13 6h8" stroke="var(--accent)" stroke-width="2"/></svg>
  <div class="contact-item" style="left:842px">
    <div class="contact-label">Contact Us</div>
    <div class="contact-value">+000 0000 0000</div>
  </div>

  <p class="copyright">© 2020 website - All rights reserved</p>
</div>
</body>
</html>
```